Bright Harbour Electrical Limited needs advertisement brochure

We require a brochure with details of the services we provide. We have just become the only approved installer for VRN products on the Isle of Man and want to feature their producst heavily in the brochure centre pages. We estimate it will be 8 pages of A5 and we would like it to be landscape please. We have all the required content as per the word doc attached and just need it to be made to look professional. It doesn't need to include all the attached pictures and only certain information from the VRN brochure needs to be included (i.e the first couple of pages of write up).
Front Page - Just the Bright Harbour main logo and pics of vans
Page 2 - About us and the logos for who we are approved by (Manx Trade Guild etc)
Page 3 - Domestic Electrical Services as per the word doc attached (those pictures don't have to be used so if you find better ones please go ahead and use).
Page 4 & 5 (Centre Pages) VRN information. Please make it clear that we are the only approved installers of their products on the Isle of Man.
Page 6 & 7 - Commercial Services as per the word doc attached (again if you can find better pictures than the ones contained in the word doc then feel free to use).
Page 8 - Back page to contain all our contact information.

Target Market(s)

Domestic and commercial customers. A design install and maintain company. Facility maintenance, preventative maintenance, fire alarm and emergency lighting contracts, home automation and sound system. Project management.

Industry/Entity Type

Electrical

Requirements
Must have
• Must be professional and appeal to both domestic and commercial customers. Has to be "BRIGHT" "EARTHY GREEN GLOBAL FEEL" like our logo shows. "CREATIVE" design. Possible similarity to our letter headed paper with part of the green globe down one side of the brochure. Must use Carlos Sanz text which is the Talvo Kessin text same as logo. Snazzy looking, eye catching, appealing. Everything you would want to get new business in the door.
Nice to have
• As above
Should not have
• Over the top tacky earthy look. After all we also wire houses that are run by horrible oil boilers (no option). Don't want to put all my egg in one basket kind of thing.

```html
<!DOCTYPE html>
<html lang="en">
<head>
<meta charset="utf-8">
<title>Bright Harbour Electrical – Brochure Spreads</title>
<link href="https://fonts.googleapis.com/css2?family=Open+Sans:wght@400;600;700&family=Roboto+Condensed:ital,wght@0,700;1,700&display=swap" rel="stylesheet">
<style>
:root{
  --green-dark:#11602e;
  --green:#1f8a3c;
  --green-light:#5cb85c;
  --ink:#333;
  --muted:#5e5e5e;
  --page:#ffffff;
  --photo-grey:#9aa3a8;
  --photo-dark:#4b5359;
}
*{box-sizing:border-box;margin:0;padding:0}
html,body{width:1200px;height:2484px;overflow:hidden;background:#fff;font-family:"Open Sans",sans-serif;color:var(--ink)}
.spread{position:absolute;left:120px;width:960px;height:580px;background:var(--page);box-shadow:0 2px 8px rgba(0,0,0,.25);display:flex;overflow:hidden}
.page{position:relative;width:480px;height:100%;padding:30px 30px}
.page+.page{border-left:1px solid #e3e3e3}
.wave{position:absolute;left:0;width:100%;pointer-events:none}
.wave.bottom{bottom:0;height:120px}
.wave.top{top:0;height:70px}
h2{font-family:"Roboto Condensed",sans-serif;color:var(--green-dark);font-size:17px;text-transform:uppercase;margin:8px 0 6px}
h3{font-family:"Roboto Condensed",sans-serif;color:var(--green);font-size:12px;text-transform:uppercase;margin:8px 0 4px}
p{font-size:8.6px;line-height:1.5;color:var(--muted);margin-bottom:6px}
.photo{background:linear-gradient(135deg,var(--photo-grey),var(--photo-dark));border-radius:2px}
.brand{font-family:"Open Sans",sans-serif;font-weight:600;color:var(--green-dark);font-size:13px}
.badge{display:inline-block;width:54px;height:30px;background:#d8e6dc;margin-right:8px;border-radius:3px}
.ticks{list-style:none;columns:2;font-size:9px;color:var(--ink);margin:4px 0 8px}
.ticks li{margin-bottom:4px;padding-left:12px;position:relative}
.ticks li:before{content:"✔";position:absolute;left:0;color:var(--green);font-size:8px}
.cols{display:flex;gap:14px}
.cols>div{flex:1}
.hero-band{position:absolute;left:0;right:0;top:300px;height:90px;background:linear-gradient(90deg,var(--green-dark),var(--green));color:#fff;text-align:center;padding-top:14px}
.hero-band .l1{font-family:"Roboto Condensed",sans-serif;font-style:italic;font-size:24px;letter-spacing:1px}
.hero-band .l2{font-family:"Roboto Condensed",sans-serif;font-style:italic;font-size:32px}
.contact-box{background:var(--green-dark);color:#fff;padding:12px;text-align:center;border-radius:3px;font-size:9px;line-height:1.6}
.contact-box strong{font-size:12px}
</style>
</head>
<body>

<!-- Spread 1: back / front cover -->
<section class="spread" style="top:10px">
  <div class="page">
    <h2 style="font-size:20px">About us</h2>
    <p>Founded in 2012, Bright Harbour Electrical Limited offers full electrical services to domestic and commercial clients across the island. Our qualified team designs, installs and maintains systems to the highest standards, from a single socket to a complete building rewire, always on time and on budget. We hold every key approval for our trade and train our staff to the latest regulations.</p>
    <p>We are proud to be the only approved installer of VRN heating products on the Isle of Man, bringing efficient renewable heating to homes and businesses.</p>
    <div style="display:flex;gap:40px;margin-top:22px">
      <div>
        <div class="brand">VRN Calder Heating</div>
        <p style="margin-top:8px">Unit 4 Harbour Park<br>Tromode Road<br>Douglas<br>Isle of Man IM1 5XX</p>
      </div>
      <div>
        <p>&#9742; 01624 555 010<br>&#9742; 01624 555 011<br>&#9993; info@brightharbour.example<br>&#9679; www.vrn-heat.example</p>
      </div>
    </div>
    <div style="margin-top:18px"><span class="badge"></span><span class="badge"></span><span class="badge"></span></div>
    <svg class="wave bottom" viewBox="0 0 480 120" preserveAspectRatio="none"><path d="M0 60 Q240 10 480 50 L480 120 L0 120Z" fill="var(--green-dark)"/><path d="M0 75 Q240 30 480 65 L480 70 Q240 40 0 85Z" fill="var(--green-light)"/></svg>
  </div>
  <div class="page">
    <div class="brand" style="text-align:center;font-size:18px;margin-top:14px">VRN Calder Heating</div>
    <div style="display:flex;justify-content:flex-end;margin-top:14px">
      <div>
        <div style="font-size:11px;font-weight:700;color:var(--green-dark);margin-bottom:6px">Approved Installers</div>
        <div style="display:flex;gap:8px">
          <div class="photo" role="img" aria-label="Heat pump indoor unit" style="width:74px;height:170px;background:linear-gradient(#f4f4f4,#c9c9c9)"></div>
          <div class="photo" role="img" aria-label="Outdoor heat pump unit" style="width:120px;height:100px;margin-top:60px;background:linear-gradient(#e8e8e8,#a9a9a9)"></div>
        </div>
      </div>
    </div>
    <div class="hero-band">
      <div class="l1">INNOVATIVE RENEWABLE</div>
      <div class="l2">Heating Solutions</div>
    </div>
    <div style="position:absolute;top:410px;width:100%;left:0;text-align:center;font-size:9px;color:var(--green-dark);font-weight:600">www.vrn-heat.example</div>
    <svg class="wave bottom" viewBox="0 0 480 120" preserveAspectRatio="none"><path d="M0 50 Q240 90 480 40 L480 120 L0 120Z" fill="var(--green-dark)"/><path d="M0 60 Q240 100 480 50 L480 56 Q240 108 0 68Z" fill="var(--green-light)"/></svg>
  </div>
</section>

<!-- Spread 2: time for change / domestic -->
<section class="spread" style="top:630px">
  <div class="page" style="padding-top:80px">
    <svg class="wave top" viewBox="0 0 480 70" preserveAspectRatio="none"><path d="M0 0 L480 0 L480 40 Q240 70 0 35Z" fill="var(--green-dark)"/><path d="M0 40 Q240 75 480 45 L480 50 Q240 80 0 46Z" fill="var(--green-light)"/></svg>
    <h2>Time for change</h2>
    <p>We all know that the way we heat our homes must change. Rising fuel costs and tighter rules mean many households are looking for cleaner, cheaper heating that still keeps every room warm through the winter months, without large changes to their home.</p>
    <p>The VRN range uses proven heat pump technology to draw warmth from the outside air, giving high efficiency all year round. Units are compact, quiet and simple to control, and they work well with radiators or underfloor heating in new or older homes alike.</p>
    <p>Each system can also provide hot water for the whole house, stored in a well insulated cylinder that is ready whenever you need it. Smart controls let you set the heating from your phone and check how much energy you are using.</p>
    <p>As approved installers we survey your property, size the system correctly and handle the full fit, so you can enjoy lower bills with complete peace of mind.</p>
    <div style="display:flex;gap:10px;margin-top:10px">
      <div class="photo" role="img" aria-label="Heat pump indoor cylinder unit" style="width:100px;height:150px"></div>
      <div class="photo" role="img" aria-label="Control panel close-up" style="width:100px;height:150px"></div>
      <div class="photo" role="img" aria-label="Outdoor unit beside a house" style="width:200px;height:150px"></div>
    </div>
  </div>
  <div class="page" style="padding-top:80px">
    <svg class="wave top" viewBox="0 0 480 70" preserveAspectRatio="none"><path d="M0 0 L480 0 L480 30 Q240 65 0 40Z" fill="var(--green-dark)"/><path d="M0 45 Q240 70 480 35 L480 40 Q240 76 0 50Z" fill="var(--green-light)"/></svg>
    <h2>Domestic electrical services</h2>
    <p>Bright Harbour Electrical Limited is experienced in all domestic work, from the smallest job to a whole new installation. Every job is carried out safely, neatly and to current regulations, and all work is certified on completion. We leave your home clean and tidy.</p>
    <h3>Fault finding, repair &amp; re-wiring</h3>
    <div style="display:flex;gap:12px">
      <div class="photo" role="img" aria-label="Electrician testing a consumer unit" style="width:150px;height:110px;flex:none"></div>
      <p>We trace faults quickly and repair them properly. Where older wiring is unsafe we offer full or partial rewires with minimal disruption to your home, and we can upgrade consumer units to the latest safety standard.</p>
    </div>
    <h3>Installations and lighting</h3>
    <div style="display:flex;gap:12px">
      <div class="photo" role="img" aria-label="Modern kitchen with downlights" style="width:150px;height:110px;flex:none"></div>
      <p>From extra sockets to feature lighting, garden power and home automation, we design and install systems that suit the way you live. We also fit sound systems, data points and electric vehicle chargers.</p>
    </div>
  </div>
</section>

<!-- Spread 3: installers / commercial -->
<section class="spread" style="top:1250px">
  <div class="page">
    <p>Heat pumps are the future for homes that need low running costs and reliable comfort. The VRN range is built for our climate and backed by a full warranty when fitted by an approved installer such as our team.</p>
    <div style="display:flex;gap:10px;margin:6px 0">
      <div class="photo" role="img" aria-label="Heat pump product" style="width:80px;height:90px"></div>
      <div class="photo" role="img" aria-label="Heating controls" style="width:80px;height:90px"></div>
    </div>
    <h2>Installers</h2>
    <ul class="ticks">
      <li>Survey and design</li><li>Full installation</li><li>Commissioning</li><li>Annual servicing</li><li>Warranty support</li><li>Repairs and parts</li>
    </ul>
    <h2>Energy related products (ERP)</h2>
    <h3>Energy related Products (ERP)</h3>
    <p>New rules on energy labelling mean every heating product now shows a clear efficiency rating. VRN units achieve top ratings, helping you choose with confidence and cut your running costs year after year. The label also shows sound levels and heat output.</p>
    <h3>Individual product and package labelling</h3>
    <p>When a heat pump is combined with controls and a cylinder, the whole package is rated. We supply the correct label for your system so you know exactly how it will perform, and we explain each figure in plain language before any work begins.</p>
    <p>Ask our team for a free survey and a clear quote for your home.</p>
  </div>
  <div class="page" style="padding-top:80px">
    <svg class="wave top" viewBox="0 0 480 70" preserveAspectRatio="none"><path d="M0 0 L480 0 L480 40 Q240 70 0 35Z" fill="var(--green-dark)"/><path d="M0 40 Q240 75 480 45 L480 50 Q240 80 0 46Z" fill="var(--green-light)"/></svg>
    <h2>Commercial electrical services</h2>
    <p>We work with offices, shops, factories and public buildings across the island. Our team handles design, installation and planned maintenance so your business keeps running safely with no unexpected downtime.</p>
    <p>We also offer project management for larger schemes, working alongside builders and contractors from first drawings to final handover, with one point of contact throughout.</p>
    <h3>Energy related products (ERP)</h3>
    <div style="display:flex;gap:12px">
      <div class="photo" role="img" aria-label="Yellow electrical test meter" style="width:160px;height:120px;flex:none;background:linear-gradient(135deg,#e7c33a,#6f6a3a)"></div>
      <div>
        <h3 style="margin-top:0">Emergency lighting</h3>
        <p>Emergency lighting is a legal requirement in most commercial premises. We design, install and test systems to keep your staff and visitors safe if the power fails, and keep full records for your inspections.</p>
      </div>
    </div>
  </div>
</section>

<!-- Spread 4: maintenance / contact -->
<section class="spread" style="top:1870px">
  <div class="page">
    <div class="cols">
      <div>
        <h3>Fire alarm maintenance</h3>
        <p>Fire alarm systems must be checked regularly to stay compliant. We offer service contracts that include routine testing, battery checks and a full log of every visit.</p>
        <div class="photo" role="img" aria-label="Fire alarm call point" style="height:130px;margin:6px 0;background:linear-gradient(135deg,#d23b3b,#6a2020)"></div>
        <h3>Security alarms</h3>
        <p>We install and maintain intruder alarms, door entry and CCTV systems that protect your property day and night. Systems can be monitored remotely and checked from your phone.</p>
      </div>
      <div>
        <p>Planned preventative maintenance keeps your systems reliable and avoids costly breakdowns. We tailor a schedule to your site and budget.</p>
        <p>Our engineers carry out thermal imaging, load checks and visual inspections, reporting clearly on any work needed.</p>
        <div class="photo" role="img" aria-label="Engineer inspecting a distribution board" style="height:130px;margin:6px 0"></div>
        <p>Contracts can combine fire, emergency lighting and security into one simple agreement with a single point of contact.</p>
      </div>
    </div>
  </div>
  <div class="page">
    <h2>New lighting and power systems</h2>
    <div class="cols">
      <div>
        <p>Modern LED lighting cuts energy use and maintenance. We design layouts that meet light levels and look great in any workspace.</p>
        <div class="photo" role="img" aria-label="Office with LED panel lighting" style="height:110px;margin:6px 0"></div>
        <h3>Electrical testing</h3>
        <p>Periodic inspection and testing confirms your installation is safe. We provide full certificates and clear advice on any remedial work.</p>
      </div>
      <div>
        <p>New power systems for extensions, fit-outs and machinery are planned carefully to suit your load and future growth.</p>
        <p>We keep disruption low by working out of hours when needed, so your business can carry on as normal.</p>
        <div class="contact-box" style="margin-top:30px">
          <strong>Contact us</strong><br>
          01624 555 010<br>
          info@brightharbour.example<br>
          www.vrn-heat.example
        </div>
      </div>
    </div>
    <svg class="wave bottom" viewBox="0 0 480 120" preserveAspectRatio="none" style="height:60px"><path d="M0 60 Q240 20 480 50 L480 120 L0 120Z" fill="var(--green-dark)"/></svg>
  </div>
</section>

</body>
</html>
```